Velmora Biz Card 2019

New business card for Velmora Property Inspections. We are a residential home inspection company in Arizona.

Target Market(s)

Real Estate

Font styles to use
Sans Serif

Requirements
Must have
• Glen Mirewick
• Home Inspector
• Velmora Property Inspections, LLC
• 480-555-0172
• glen@velmora-llc.example

```html
<!DOCTYPE html>
<html lang="en">
<head>
<meta charset="utf-8">
<title>Velmora Biz Card 2019</title>
<link href="https://fonts.googleapis.com/css2?family=Open+Sans:wght@400;600;700&display=swap" rel="stylesheet">
<style>
  :root {
    --backdrop: #e8e7e3;
    --card: #ffffff;
    --green: #4fb748;
    --slate: #6d6e71;
    --ink: #111111;
  }
  * { margin: 0; padding: 0; box-sizing: border-box; }
  html, body { width: 1200px; height: 1200px; overflow: hidden; }
  body {
    background: var(--backdrop);
    font-family: "Open Sans", Arial, sans-serif;
    position: relative;
  }
  .card {
    position: absolute;
    background: var(--card);
    border-radius: 48px 8px 8px 48px;
    overflow: hidden;
  }
  .card--front { left: 233px; top: 156px; width: 731px; height: 418px; }
  .card--back  { left: 234px; top: 626px; width: 732px; height: 424px; }

  .card__band {
    position: absolute; left: 0; top: 0; bottom: 0; width: 150px;
    background: linear-gradient(90deg, var(--green) 0%, var(--green) 70%, var(--slate) 100%);
  }

  .brand__dot {
    position: absolute; left: 398px; top: 118px;
    width: 70px; height: 70px; border-radius: 50%;
    background: var(--green);
  }
  .brand__name {
    position: absolute; left: 183px; width: 500px; top: 236px;
    text-align: center;
    font-weight: 700; font-size: 46px; line-height: 1;
    letter-spacing: 3px; color: var(--slate);
  }

  .line { position: absolute; line-height: 1; white-space: nowrap; color: var(--ink); }
  .person__name { left: 166px; top: 40px; font-size: 37px; font-weight: 400; }
  .person__rule {
    position: absolute; left: 166px; top: 85px;
    width: 416px; height: 2.5px; background: var(--ink);
  }
  .person__role    { left: 167px; top: 108px; font-size: 25px; }
  .person__company { left: 167px; top: 139px; font-size: 25px; }
  .contact__title {
    left: 230px; top: 206px; font-size: 37px; font-weight: 600; color: var(--green);
  }
  .contact__icon {
    position: absolute; left: 294px; width: 32px; height: 32px;
  }
  .contact__text { left: 344px; font-size: 23px; }
</style>
</head>
<body>

  <section class="card card--front">
    <div class="card__band" role="img" aria-label="Green and grey decorative wave along the card's left edge"></div>
    <div class="brand__dot"></div>
    <div class="brand__name">VELMORA</div>
  </section>

  <section class="card card--back">
    <div class="card__band" role="img" aria-label="Green and grey decorative wave along the card's left edge"></div>

    <h1 class="line person__name">Glen Mirewick</h1>
    <div class="person__rule"></div>
    <p class="line person__role">Home Inspector</p>
    <p class="line person__company">Velmora Property Inspections, LLC</p>

    <h2 class="line contact__title">Get in touch</h2>

    <svg class="contact__icon" style="top:263px" viewBox="0 0 32 32" aria-hidden="true">
      <circle cx="16" cy="16" r="16" fill="var(--green)"/>
      <path d="M10.5 8.5l3 0 1.3 4-2 1.5c1 2.2 2.6 3.8 4.8 4.8l1.5-2 4 1.3v3c0 1-.8 1.6-1.7 1.5C14.5 22 10 17.5 9 11.2c-.1-.9.5-2.7 1.5-2.7z" fill="#fff"/>
    </svg>
    <p class="line contact__text" style="top:269px">480-555-0172</p>

    <svg class="contact__icon" style="top:312px" viewBox="0 0 32 32" aria-hidden="true">
      <circle cx="16" cy="16" r="16" fill="var(--green)"/>
      <g fill="none" stroke="#fff" stroke-width="1.4">
        <circle cx="16" cy="16" r="7.5"/>
        <ellipse cx="16" cy="16" rx="3.2" ry="7.5"/>
        <line x1="8.5" y1="16" x2="23.5" y2="16"/>
        <line x1="9.5" y1="12" x2="22.5" y2="12"/>
        <line x1="9.5" y1="20" x2="22.5" y2="20"/>
      </g>
    </svg>
    <p class="line contact__text" style="top:317px">www.velmora-llc.example</p>

    <svg class="contact__icon" style="top:359px" viewBox="0 0 32 32" aria-hidden="true">
      <circle cx="16" cy="16" r="16" fill="var(--green)"/>
      <g fill="none" stroke="#fff" stroke-width="1.4">
        <rect x="9" y="11" width="14" height="10"/>
        <path d="M9 11l7 6 7-6M9 21l5-5M23 21l-5-5"/>
      </g>
    </svg>
    <p class="line contact__text" style="top:363px">glen@velmora-llc.example</p>
  </section>

</body>
</html>
```